Brindlecove Plumbing Solutions

This is for my new plumbing company, I have attached an example of what I’m going for but want it to look better.

Target Market(s)

Home owners, real estate, etc.

Industry/Entity Type

Plumbing

Other font styles liked:
• As per my logo and other examples uploaded

Colors

Designer to choose colors to be used in the design.

Requirements
Must have
• Must include my logo provided and similar to my flyer I have attached but better

```html
<!DOCTYPE html>
<html lang="en">
<head>
<meta charset="utf-8">
<title>Brindlecove Plumbing Solutions – Flyer</title>
<link href="https://fonts.googleapis.com/css2?family=Fredoka:wght@500;600;700&family=Arimo:wght@400&display=swap" rel="stylesheet">
<style>
  :root{
    --page:#e9e6e2;
    --charcoal:#3e3e3f;
    --sky:#6fa8dc;
    --sky-deep:#5a96cf;
    --orange:#f08a2c;
    --white:#ffffff;
    --pill:#4a4a4b;
    --silver:#d9dcdf;
    --ink:#2f3742;
  }
  *{margin:0;padding:0;box-sizing:border-box}
  html,body{width:1200px;height:800px;overflow:hidden;background:var(--page)}
  .flyer{position:absolute;left:309px;top:20px;width:582px;height:760px;background:var(--charcoal);overflow:hidden;font-family:"Fredoka",sans-serif;color:var(--white)}
  .offer-disc{position:absolute;left:325px;top:-282px;width:564px;height:564px;border-radius:50%;background:var(--sky)}
  .offer{position:absolute;left:366px;top:14px;width:200px;text-align:center}
  .offer-lead{font-weight:600;font-size:22px;line-height:27px;color:var(--white)}
  .offer-figure{font-weight:600;font-size:68px;line-height:66px;color:var(--silver);letter-spacing:1px}
  .offer-word{font-weight:700;font-size:28px;line-height:30px;color:var(--ink);letter-spacing:1px}
  .brand{position:absolute;left:14px;top:34px;display:flex;align-items:center;gap:10px}
  .brand-mark{width:40px;height:40px;border-radius:50%;background:var(--sky)}
  .brand-name{font-weight:600;font-size:18px;line-height:21px;color:var(--white)}
  .services-frame{position:absolute;left:0;top:0;width:582px;height:300px;pointer-events:none}
  .services-title{position:absolute;left:43px;top:134px;font-weight:700;font-size:23px;line-height:28px;letter-spacing:.5px}
  .service{position:absolute;width:128px;height:93px;border-radius:9px;display:flex;align-items:center;justify-content:center;text-align:center;font-weight:600;font-size:16.5px;line-height:20px;padding-top:12px}
  .service--primary{background:var(--sky);color:var(--white);width:153px}
  .service--standard{background:var(--white);color:var(--sky-deep);border:3px solid var(--orange)}
  .service-icon{position:absolute;left:50%;top:-22px;margin-left:-21px;width:42px;height:42px}
  .col1{left:51px}.col2{left:219px}.col3{left:362px}
  .row1{top:185px}.row2{top:310px}.row3{top:445px}
  .contact{position:absolute;left:0;top:597px;width:582px;height:163px;background:var(--sky)}
  .contact-title{position:absolute;left:56px;top:12px;font-weight:600;font-size:17px}
  .contact-pill{position:absolute;height:32px;border-radius:16px;background:var(--pill);display:flex;align-items:center;gap:10px;padding-left:22px;font-family:"Arimo",sans-serif;font-size:15px}
  .contact-pill svg{width:16px;height:16px;flex:none}
  .pill-phone{left:20px;top:44px;width:219px}
  .pill-mail{left:22px;top:83px;width:353px}
  .pill-web{left:23px;top:125px;width:282px}
  .socials{position:absolute;left:420px;top:102px;display:flex;flex-direction:column;gap:6px}
  .social{display:flex;align-items:center;gap:6px;font-weight:600;font-size:14px;color:var(--white)}
  .social-dot{width:18px;height:18px;border-radius:50%;background:var(--white)}
</style>
</head>
<body>
<main class="flyer">
  <div class="offer-disc"></div>

  <div class="brand">
    <span class="brand-mark"></span>
    <span class="brand-name">Brindlecove<br>Plumbing Solutions</span>
  </div>

  <div class="offer">
    <p class="offer-lead">Mention this<br>flyer to receive</p>
    <p class="offer-figure">15%</p>
    <p class="offer-word">DISCOUNT</p>
  </div>

  <svg class="services-frame" viewBox="0 0 582 300">
    <path d="M245 137 Q245 122 232 122 L30 122 Q20 122 20 132 L20 224 Q20 234 30 234 L51 234" fill="none" stroke="var(--orange)" stroke-width="2.5"/>
    <line x1="204" y1="234" x2="219" y2="234" stroke="var(--orange)" stroke-width="2.5"/>
    <line x1="283" y1="149" x2="357" y2="149" stroke="var(--orange)" stroke-width="2"/>
  </svg>
  <h2 class="services-title">OUR SERVICES</h2>

  <div class="service service--primary col1 row1">
    <svg class="service-icon" viewBox="0 0 42 42"><circle cx="21" cy="21" r="20" fill="var(--sky)"/><circle cx="21" cy="21" r="15" fill="none" stroke="var(--white)" stroke-width="2.5"/><text x="21" y="25" text-anchor="middle" font-family="Fredoka,sans-serif" font-size="11" font-weight="600" fill="var(--white)">24/7</text></svg>
    Emergency<br>Plumbing
  </div>
  <div class="service service--standard col2 row1">
    <svg class="service-icon" viewBox="0 0 42 42"><circle cx="21" cy="21" r="20" fill="var(--orange)"/><path d="M12 27 L24 15 M22 13 a5 5 0 1 0 7 7" stroke="var(--white)" stroke-width="3" fill="none" stroke-linecap="round"/></svg>
    Plumbing<br>Maintenance
  </div>
  <div class="service service--standard col3 row1">
    <svg class="service-icon" viewBox="0 0 42 42"><circle cx="21" cy="21" r="20" fill="var(--orange)"/><path d="M12 10 V22 Q12 30 20 30 H30 V22" stroke="var(--white)" stroke-width="4" fill="none"/></svg>
    Draining<br>Maintenance
  </div>

  <div class="service service--primary col1 row2">
    <svg class="service-icon" viewBox="0 0 42 42"><circle cx="21" cy="21" r="20" fill="var(--sky)"/><path d="M21 9 C27 16 29 20 29 24 a8 8 0 0 1 -16 0 C13 20 17 17 21 9Z" fill="var(--white)"/></svg>
    Gas<br>Maintenance
  </div>
  <div class="service service--standard col2 row2">
    <svg class="service-icon" viewBox="0 0 42 42"><circle cx="21" cy="21" r="20" fill="var(--orange)"/><rect x="14" y="9" width="14" height="24" rx="2" fill="var(--white)"/><circle cx="21" cy="16" r="3" fill="var(--sky-deep)"/></svg>
    Hot water<br>Systems
  </div>
  <div class="service service--standard col3 row2">
    <svg class="service-icon" viewBox="0 0 42 42"><circle cx="21" cy="21" r="20" fill="var(--orange)"/><path d="M11 12 H24 Q28 12 28 16 V20" stroke="var(--white)" stroke-width="4" fill="none"/><path d="M28 25 q-3 4 0 6 q3 -2 0 -6Z" fill="var(--white)"/></svg>
    Leaking<br>Fixtures
  </div>

  <div class="service service--primary col1 row3">
    <svg class="service-icon" viewBox="0 0 42 42"><circle cx="21" cy="21" r="20" fill="var(--sky)"/><path d="M12 13 H28 Q32 13 32 17 Q32 21 28 21 H14 Q10 21 10 25 Q10 29 14 29 H30" stroke="var(--white)" stroke-width="2.5" fill="none"/></svg>
    Blocked sewer<br>&amp; stormwater
  </div>
  <div class="service service--standard col2 row3">
    <svg class="service-icon" viewBox="0 0 42 42"><circle cx="21" cy="21" r="20" fill="var(--orange)"/><path d="M21 33 C14 25 12 21 12 17 a9 9 0 0 1 18 0 C30 21 28 25 21 33Z" fill="var(--white)"/><circle cx="21" cy="17" r="3.5" fill="var(--orange)"/></svg>
    Camera &amp;<br>locating
  </div>
  <div class="service service--standard col3 row3">
    <svg class="service-icon" viewBox="0 0 42 42"><circle cx="21" cy="21" r="20" fill="var(--orange)"/><rect x="18" y="8" width="6" height="20" rx="3" fill="var(--white)"/><circle cx="21" cy="29" r="5" fill="var(--white)"/><rect x="20" y="15" width="2" height="14" fill="var(--sky-deep)"/></svg>
    TMV<br>maintenance
  </div>

  <section class="contact">
    <h3 class="contact-title">Contact Us</h3>
    <div class="contact-pill pill-phone">
      <svg viewBox="0 0 16 16"><path d="M3 1 L6 1 L7 5 L5 6 Q6 9 10 11 L11 9 L15 10 L15 13 Q15 15 13 15 Q2 14 1 3 Q1 1 3 1Z" fill="var(--white)"/></svg>
      0400 318 274
    </div>
    <div class="contact-pill pill-mail">
      <svg viewBox="0 0 16 16"><rect x="1" y="3" width="14" height="10" rx="1.5" fill="var(--white)"/><path d="M1.5 4 L8 9 L14.5 4" stroke="var(--pill)" stroke-width="1.5" fill="none"/></svg>
      hello@brindlecoveplumbing.net
    </div>
    <div class="contact-pill pill-web">
      <svg viewBox="0 0 16 16"><circle cx="8" cy="8" r="6.5" fill="none" stroke="var(--white)" stroke-width="1.4"/><ellipse cx="8" cy="8" rx="3" ry="6.5" fill="none" stroke="var(--white)" stroke-width="1.2"/><line x1="1.5" y1="8" x2="14.5" y2="8" stroke="var(--white)" stroke-width="1.2"/></svg>
      @brindlecovePlumbing
    </div>
    <div class="socials">
      <span class="social"><span class="social-dot"></span>Facelink</span>
      <span class="social"><span class="social-dot"></span>Pictorama</span>
    </div>
  </section>
</main>
</body>
</html>
```